Rear Window Advertisement and Magnets for side doors

Questions about Solvanta insurance?
Ask me, I'm a nurse
629-###-####
(Disclaimer.................in small print....)

```html
<!DOCTYPE html>
<html lang="en">
<head>
<meta charset="utf-8">
<title>Solvanta Insurance Rear Window Decal</title>
<link rel="stylesheet" href="https://fonts.googleapis.com/css2?family=Gochi+Hand&family=Kanit:wght@600&family=Noto+Serif:wght@700&display=swap">
<style>
  :root {
    --bg: #000000;
    --pink: #c8669e;
    --ink: #000000;
    --white: #ffffff;
    --portrait: #d3cdc3;
  }
  html, body {
    margin: 0;
    padding: 0;
    width: 1072px;
    height: 1200px;
    overflow: hidden;
    background: var(--bg);
  }
  .canvas {
    position: relative;
    width: 1072px;
    height: 1200px;
    background: var(--bg);
  }
  .decal {
    position: absolute;
    left: 65px;
    top: 418px;
    width: 942px;
    height: 364px;
  }
  .decal-shapes {
    position: absolute;
    left: 0;
    top: 0;
    width: 942px;
    height: 364px;
  }
  .headline {
    position: absolute;
    left: 32px;
    top: -8px;
    margin: 0;
    font-family: "Gochi Hand", cursive;
    font-weight: 400;
    font-size: 62px;
    line-height: 58px;
    color: var(--pink);
    letter-spacing: 1px;
    white-space: nowrap;
  }
  .tagline {
    position: absolute;
    left: 60px;
    top: 141px;
    width: 460px;
    height: 80px;
    margin: 0;
    font-family: "Kanit", sans-serif;
    font-weight: 600;
    font-size: 53px;
    line-height: 80px;
    color: var(--white);
    white-space: nowrap;
  }
  .phone {
    position: absolute;
    left: 32px;
    top: 218px;
    margin: 0;
    font-family: "Noto Serif", serif;
    font-weight: 700;
    font-size: 88px;
    line-height: 1;
    letter-spacing: -2px;
    color: var(--white);
    white-space: nowrap;
  }
  .disclaimer {
    position: absolute;
    left: 28px;
    top: 330px;
    margin: 0;
    font-family: Arial, Helvetica, sans-serif;
    font-style: italic;
    font-size: 16px;
    line-height: 1;
    color: var(--white);
    white-space: nowrap;
  }
</style>
</head>
<body>
<main class="canvas">
  <section class="decal">
    <svg class="decal-shapes" viewBox="150 120 1520 587" width="942" height="364">
      <path class="decal-band" fill="var(--pink)"
        d="M150 423 H197 V333 H1025 V423 H1670 V667 Q1670 707 1630 707 H190 Q150 707 150 667 Z"/>
      <rect class="tagline-box" x="212" y="348" width="798" height="130" fill="var(--ink)"/>
      <polygon class="speech-tail" points="1010,373 1113,375 1010,478" fill="var(--ink)"/>
      <polygon class="speech-tail-stripe" points="1016,462 1088,398 1022,472" fill="var(--pink)"/>
      <circle class="nurse-portrait" cx="1346" cy="400" r="280" fill="var(--portrait)"
        role="img" aria-label="Illustration of a smiling nurse with purple hair, white coat and stethoscope, raising one finger"/>
    </svg>
    <h1 class="headline">Questions about<br>Solvanta insurance?</h1>
    <p class="tagline">Ask me, I'm a nurse</p>
    <p class="phone">629-417-2593</p>
    <p class="disclaimer">Disclaimer: Lorem ipsum dolor sit amet, consectetur adipiscing elitconsectetur</p>
  </section>
</main>
</body>
</html>
```